Quillmark Hall Business Card

I need a business card design. We are a collaborate online training company. Our colors are gray and green. Our website is QuillmarkHall.com

I would like an area for a profile picture within the card

```html
<!DOCTYPE html>
<html lang="en">
<head>
<meta charset="utf-8">
<title>Quillmark Hall Business Card</title>
<link rel="stylesheet" href="https://fonts.googleapis.com/css2?family=Fira+Sans+Extra+Condensed:wght@700&family=Source+Sans+3:wght@400;600;700&display=swap">
<style>
  :root {
    --backdrop: #141414;
    --card-white: #ffffff;
    --brand-green: #84c13c;
    --ink: #111111;
    --ink-soft: #222222;
    --photo-top: #8a8a8a;
    --photo-bottom: #4a4a4a;
  }
  * { margin: 0; padding: 0; box-sizing: border-box; }
  html, body {
    width: 1200px; height: 900px; overflow: hidden;
    background: var(--backdrop);
  }
  .stage { position: relative; width: 1200px; height: 900px; }

  .card {
    position: absolute; top: 170px; width: 347px; height: 561px; overflow: hidden;
  }
  .card-front { left: 259px; background: var(--card-white); }
  .card-back { left: 631px; background: var(--brand-green); }

  .accent-tab {
    position: absolute; left: 101px; width: 144px; background: var(--brand-green);
  }
  .accent-tab.top { top: 0; height: 30px; }
  .accent-tab.bottom { bottom: 0; height: 28px; }

  .wordmark {
    position: absolute; left: 0; width: 100%; text-align: center;
    font-family: "Fira Sans Extra Condensed", "Arial Narrow", sans-serif;
    font-weight: 700; letter-spacing: -0.5px; line-height: 1;
  }
  .card-front .wordmark { top: 92px; font-size: 54px; color: var(--ink); }

  .details {
    position: absolute; left: 0; width: 100%; text-align: center;
    font-family: "Source Sans 3", "Myriad Pro", sans-serif; color: var(--ink-soft);
  }
  .person-name { top: 212px; font-size: 23px; font-weight: 600; color: var(--brand-green); }
  .person-role { top: 239px; font-size: 15px; }
  .contact-lines { top: 297px; font-size: 15px; line-height: 20px; }
  .address-lines { top: 383px; font-size: 15px; line-height: 20px; }
  .web-address { top: 453px; font-size: 15px; font-weight: 700; color: var(--ink); }

  .back-logo {
    position: absolute; top: 140px; left: 24px; display: flex; align-items: center; gap: 14px;
  }
  .back-logo .mark-dot { width: 44px; height: 44px; border-radius: 50%; background: var(--card-white); }
  .back-logo .wordmark-text {
    font-family: "Fira Sans Extra Condensed", "Arial Narrow", sans-serif;
    font-weight: 700; font-size: 46px; line-height: 1; color: var(--card-white); letter-spacing: -0.5px;
  }

  .profile-photo {
    position: absolute; left: 0; bottom: 0; width: 250px; height: 282px;
    background: linear-gradient(180deg, var(--photo-top), var(--photo-bottom));
  }
</style>
</head>
<body>
<main class="stage">
  <section class="card card-front" aria-label="Card front">
    <div class="accent-tab top"></div>
    <h1 class="wordmark">QuillmarkHall</h1>
    <p class="details person-name">Marcus Ellery</p>
    <p class="details person-role">Managing Director</p>
    <p class="details contact-lines">(044) 555 218 407<br>(044) 555218408<br>hello@quillmarkhall.com</p>
    <p class="details address-lines">88 Lantern Row,<br>Brightmoor, 40512</p>
    <p class="details web-address">www.quillmarkhall.com</p>
    <div class="accent-tab bottom"></div>
  </section>

  <section class="card card-back" aria-label="Card back">
    <div class="back-logo">
      <span class="mark-dot"></span>
      <span class="wordmark-text">QuillmarkHall</span>
    </div>
    <div class="profile-photo" role="img" aria-label="Profile photo of the managing director"></div>
  </section>
</main>
</body>
</html>
```